New Design required for Disposable Gloves Pack

We need a new design for our range of disposable Gloves.
The brand name is "Pardo" I will attach the existing logo.

The needs to be 3 variations of the design (maybe different colours) that we can use for the different kinds of gloves: Latex Gloves, Clear Vinyl Gloves & Blue Vinyl Gloves.
Pack size is: 220x65x120mm.

Attached is a template to use showing all sides of the pack as flat. It is preferable that you supply an image of the complete folded pack as well with your design. Also attached is a PDF of our old pack design. Please use all the text on this old design for the new one.

The packs need to be easily differentiated from each other.

Target Market(s)

New Zealand Businesses, food processors & manufacturers. Medical & health care professionals

Font styles to use
Sans Serif

Requirements
Must have
• 3 variations of the same pack design to differentiate between the 3 types of gloves we offer: Latex Gloves, Clear Vinyl & Blue Vinyl Gloves.

```html
<!DOCTYPE html>
<html lang="en">
<head>
<meta charset="utf-8">
<title>Pardo Blue Vinyl Gloves – Pack Net</title>
<link rel="stylesheet" href="https://fonts.googleapis.com/css2?family=Josefin+Sans:wght@400;600;700&display=swap">
<style>
  :root {
    --stage: #3b3b3b;
    --teal-deep: #1b5e67;
    --teal-light: #55b2a8;
    --paper: #ffffff;
    --brand-green: #86ad37;
    --hairline: rgba(255,255,255,0.75);
    --perforation: #1b5e67;
  }
  * { box-sizing: border-box; margin: 0; padding: 0; }
  html, body { width: 1200px; height: 1000px; overflow: hidden; }
  body {
    background: var(--stage);
    font-family: "Josefin Sans", "Gill Sans", sans-serif;
    position: relative;
  }
  .panel { position: absolute; overflow: hidden; }
  .panel svg.panel-art { position: absolute; inset: 0; }

  /* Top lid */
  .lid { left: 330px; top: 150px; width: 770px; height: 227px; background: var(--teal-deep); }
  .lid-content {
    position: absolute; inset: 0; transform: rotate(180deg);
    display: flex; align-items: flex-start; justify-content: space-between;
    padding: 38px 60px 0 70px; color: var(--paper);
  }
  .lid-brand { font-size: 40px; font-weight: 600; letter-spacing: 2px; }
  .lid-features { display: flex; gap: 46px; font-size: 15px; padding-top: 60px; }
  .lid-features li { list-style: none; }

  /* End panel */
  .end { left: 100px; top: 380px; width: 227px; height: 420px; background: var(--teal-deep); }
  .size-badge {
    position: absolute; left: 118px; top: 40px; width: 62px; height: 62px; border-radius: 50%;
    background: var(--teal-light); color: var(--paper);
    font-size: 32px; font-weight: 700; display: flex; align-items: center; justify-content: center;
    padding-top: 5px;
  }
  .end-text {
    position: absolute; left: 40px; top: 110px; width: 290px;
    transform-origin: 0 0; transform: translate(170px, 0) rotate(90deg);
    color: var(--paper);
  }
  .end-title { font-size: 27px; font-weight: 700; letter-spacing: 1px; }
  .end-contact { font-size: 14px; margin-top: 16px; line-height: 1.7; }

  /* Front face */
  .front { left: 330px; top: 380px; width: 770px; height: 420px; background: var(--paper); }
  .front-title {
    position: absolute; left: 28px; bottom: 22px; color: var(--paper);
    font-size: 31px; font-weight: 700;
  }
  .brand-mark {
    position: absolute; right: 36px; top: 46px; display: flex; align-items: center; gap: 12px;
    color: var(--brand-green); font-size: 52px; font-weight: 600; letter-spacing: 4px;
  }
  .brand-mark .dot { width: 20px; height: 20px; border-radius: 50%; background: var(--brand-green); }
  .dispenser-opening {
    position: absolute; left: 210px; top: 130px; width: 430px; height: 140px;
    border: 2px dashed var(--perforation); border-radius: 40px;
  }
  .pack-count {
    position: absolute; right: 40px; bottom: 30px; display: flex; align-items: flex-end; gap: 12px;
    color: var(--teal-deep); font-weight: 700; font-size: 19px; line-height: 1.15;
  }
  .pack-count .count-icon {
    width: 58px; height: 58px; border-radius: 50%; background: var(--teal-light);
    border: 2px solid var(--teal-deep); margin-bottom: 30px;
  }
</style>
</head>
<body>
  <section class="panel lid" aria-label="Top lid">
    <svg class="panel-art" viewBox="0 0 770 227" aria-hidden="true">
      <path d="M0,0 H260 L0,120 Z" fill="var(--teal-light)"/>
      <path d="M0,150 C250,70 520,60 770,40" fill="none" stroke="var(--hairline)" stroke-width="1.5"/>
      <path d="M0,175 C280,110 560,80 770,70" fill="none" stroke="var(--hairline)" stroke-width="1"/>
    </svg>
    <div class="lid-content">
      <span class="lid-brand">Pardo</span>
      <ul class="lid-features">
        <li>✓ Large</li>
        <li>✓ Single Use</li>
        <li>✓ Ambidextrous</li>
        <li>✓ Lightly Powdered</li>
      </ul>
    </div>
  </section>

  <section class="panel end" aria-label="End panel">
    <svg class="panel-art" viewBox="0 0 227 420" aria-hidden="true">
      <path d="M0,0 H30 C10,140 10,280 30,420 H0 Z" fill="var(--teal-light)"/>
      <path d="M60,0 C20,140 20,280 60,420" fill="none" stroke="var(--hairline)" stroke-width="1.2"/>
      <path d="M75,0 C38,140 38,280 75,420" fill="none" stroke="var(--hairline)" stroke-width="1"/>
    </svg>
    <div class="size-badge">L</div>
    <div class="end-text">
      <p class="end-title">Blue Vinyl Gloves</p>
      <p class="end-contact">0800 514 306<br>www.lumavale.co.nz</p>
    </div>
  </section>

  <section class="panel front" aria-label="Front face">
    <svg class="panel-art" viewBox="0 0 770 420" aria-hidden="true">
      <path d="M0,0 H150 C40,160 230,370 620,420 H0 Z" fill="var(--teal-light)"/>
      <path d="M0,0 H128 C22,160 210,375 570,420 H0 Z" fill="var(--teal-deep)"/>
    </svg>
    <div class="brand-mark"><span class="dot"></span>Pardo</div>
    <div class="dispenser-opening"></div>
    <p class="front-title">Blue Vinyl Gloves</p>
    <div class="pack-count">
      <span>100<br>Gloves</span>
      <span class="count-icon"></span>
    </div>
  </section>
</body>
</html>
```